WEBSITE: Security Officer Training, Security Officer Certifications, Security Officer Job Training

colorful and simple website, NO FLASH, and easy for SEO
Able to Upload to GODADDY WEBSITE BUILDER!

We need a great image that depicts and sell Watchpost Learning Hub
Our websites for info: Security Officers doing cool things, the pictures must be great..

FEEL Free to choose ideas from our services in our
Www.watchpostlearninghub.org site
The CPO certified protection officer tab
The CFO certified Firearms Office tab
The Security Officer Academy
The Campus security officer
Will be a few pages, landing page and contact page..
Www.watchpostlearninghub.org
Www.civicwardcollege.net
Www.beaconcredentialsdesk.com
ALSO go to goggle and put in
Los Angles "Security Guard Training"
California Guard Card
Guard Card
Firearms Training
And similar words to see competitors websites!

WE want our more KICK ASS and COOOL!

OUr Industry: Security Officer Training Certifications
INFO: SECURITY OFFICER TRAINING
Law Enforcement
Police
Criminal Justice Training
Security Guards
Security Professional

Target Market(s)

Law Enforcement Training
Police Training
Criminal Justice Training
Security Officer Training
Security Officer Certifications

Industry/Entity Type

Security

Number of Pages Required

3 page

Requirements
Must have
• Able to upload to GODADDY WEBSITE BUILDER
• Easy to edit
• Must be easy for SEO
• NO FLASH or other things that prevent mobile phones
• MOBILE PHONE COMPATIBLE
• COOL!
• Call to action
• Contact form for email sign ups
• PICTURES SLIDE SHOW MUST HAVE
Should not have
• NO have flash

```html
<!DOCTYPE html>
<html lang="en">
<head>
<meta charset="utf-8">
<title>Watchpost Learning Hub – Security Officer Training</title>
<link rel="stylesheet" href="https://fonts.googleapis.com/css2?family=Montserrat:wght@400;600;700;800&family=Open+Sans:wght@400;600;700&display=swap">
<style>
:root{
  --orange:#d98a1b;
  --orange-dark:#b8710f;
  --gold:#f0b429;
  --ink:#1f1f1f;
  --dark:#222;
  --darker:#161616;
  --text:#555;
  --muted:#8a8a8a;
  --light:#f4f4f4;
  --white:#fff;
  --navy:#1f2f4a;
}
*{box-sizing:border-box;margin:0;padding:0}
html,body{width:1200px;height:4452px;overflow:hidden}
body{font-family:"Open Sans",Arial,sans-serif;color:var(--text);font-size:13px;background:var(--white)}
h1,h2,h3,h4,.btn,.nav a{font-family:"Montserrat",Arial,sans-serif}
section,header,footer{position:relative;width:1200px;overflow:hidden}
.wrap{width:1000px;margin:0 auto;position:relative}
.btn{display:inline-block;font-size:11px;font-weight:700;letter-spacing:.5px;padding:10px 18px;text-transform:uppercase;text-decoration:none}
.btn-orange{background:var(--orange);color:var(--white)}
.btn-outline{border:1px solid #999;color:var(--ink);background:var(--white)}
.btn-outline-light{border:1px solid #ddd;color:var(--white)}
.btn .arr{margin-left:8px}

/* top bar */
.topbar{height:40px;background:rgba(20,24,32,.92);color:#cfd3da;font-size:11px;display:flex;align-items:center;padding:0 100px;justify-content:space-between;position:absolute;top:0;left:0;z-index:3;width:1200px}
.topbar .info span{margin-right:24px}
.topbar .right{display:flex;align-items:center;gap:14px}
.topbar .dot{width:14px;height:14px;border-radius:50%;background:#5b6270;display:inline-block}
.topbar .search{width:40px;height:40px;background:var(--orange);display:flex;align-items:center;justify-content:center}

/* hero */
.hero{height:800px;background:linear-gradient(120deg,#6f8aa8 0%,#9fb4c8 35%,#4f6580 70%,#2d3c52 100%)}
.hero .scene{position:absolute;inset:0}
.hero .officer{position:absolute;right:110px;top:120px;width:330px;height:680px;background:linear-gradient(180deg,#2b2b30,#15161a);border-radius:160px 160px 0 0}
.nav{position:absolute;top:40px;left:0;width:1200px;height:90px;display:flex;align-items:center;justify-content:center;gap:34px;background:linear-gradient(180deg,rgba(16,24,38,.75),rgba(16,24,38,0))}
.nav a{color:var(--white);font-size:11px;font-weight:600;text-decoration:none;letter-spacing:.6px}
.logo{display:flex;align-items:center;gap:10px;margin:0 30px;color:var(--white);font-family:"Montserrat",sans-serif;font-weight:700;font-size:15px}
.logo i{width:56px;height:56px;border-radius:50%;background:var(--gold);display:block}
.promo{position:absolute;left:150px;top:246px}
.promo .tag{background:var(--gold);color:var(--ink);font-family:"Montserrat",sans-serif;font-weight:800;font-size:20px;padding:8px 16px;display:inline-block}
.promo .box{background:rgba(24,28,60,.85);padding:14px 18px;width:340px;color:var(--white);font-family:"Montserrat",sans-serif;font-weight:800;font-size:24px;line-height:1.2}
.promo .box b{color:var(--gold)}
.promo .box em{font-style:normal;color:var(--white)}
.promo .phone{margin-top:14px;color:var(--white);font-family:"Montserrat",sans-serif;font-weight:700;font-size:22px;display:flex;align-items:center;gap:12px}

/* about */
.about{height:290px;text-align:center;padding-top:44px}
.about h3{font-size:15px;color:var(--ink);font-weight:600}
.about h2{font-size:26px;color:var(--ink);font-weight:800;margin-top:6px}
.about p{width:740px;margin:22px auto 0;line-height:1.7;font-size:12px;color:var(--muted)}
.about .actions{margin-top:28px;display:flex;justify-content:center;gap:10px}

/* section label */
.label{display:inline-block;border-top:1px solid currentColor;border-bottom:1px solid currentColor;padding:6px 30px;text-align:center}
.label small{display:block;font-size:9px;letter-spacing:1px}
.label strong{display:block;font-family:"Montserrat",sans-serif;font-size:15px;font-weight:800;letter-spacing:1px}

/* why */
.why{height:630px;background:linear-gradient(180deg,#262626,#121212);color:#cfcfcf;text-align:center;padding-top:60px}
.why .label{color:var(--white)}
.why h2{color:var(--gold);font-size:17px;font-weight:700;margin-top:46px;line-height:1.5}
.features{display:grid;grid-template-columns:300px 260px 300px;justify-content:center;gap:30px;margin-top:40px}
.feature{display:flex;gap:14px;margin-bottom:34px;text-align:left}
.features .left .feature{flex-direction:row-reverse;text-align:right}
.feature h4{color:var(--gold);font-size:16px;font-weight:700}
.feature p{font-size:11px;line-height:1.5;margin-top:4px;color:#bdbdbd}
.feature .ico{flex:none;width:34px;height:34px;border-radius:50%;border:1px solid var(--gold)}
.badge{width:230px;height:260px;margin:10px auto 0;border-radius:46% 46% 40% 40%;background:radial-gradient(circle at 50% 40%,#e6c27a,#a07a35 60%,#5a4620)}
.why .actions{margin-top:10px;display:flex;justify-content:center;gap:10px}

/* courses */
.courses{height:640px;text-align:center;padding-top:60px}
.courses .label{color:var(--ink)}
.cards{display:flex;justify-content:center;gap:24px;margin-top:50px}
.card{width:210px;border:1px solid #e2e2e2;background:var(--white);padding-bottom:22px}
.card .photo{height:130px;background:linear-gradient(160deg,#8aa1b8,#3b4656)}
.card .ico{width:40px;height:40px;border-radius:50%;background:var(--orange);margin:-20px auto 0;border:3px solid var(--white)}
.card h4{color:var(--orange);font-size:12px;font-weight:800;margin:12px 14px 0;line-height:1.4}
.card p{font-size:10px;line-height:1.5;margin:8px 16px 14px;color:var(--muted)}
.card .btn{padding:6px 12px;font-size:9px}
.courses .register{margin-top:40px}

/* gallery */
.gallery{height:680px;background:linear-gradient(180deg,#2a2a2a,#111);text-align:center;padding-top:60px}
.gallery .label{color:var(--white)}
.video{width:620px;height:340px;margin:50px auto 0;background:linear-gradient(135deg,#3a4d68,#16202e 60%,#0c0c0c);position:relative}
.video .bar{position:absolute;top:0;left:0;right:0;height:22px;background:rgba(0,0,0,.6);color:#ddd;font-size:10px;text-align:left;padding:4px 10px}
.video .play{position:absolute;left:270px;top:140px}
.thumbs{display:flex;gap:6px;justify-content:center;margin-top:12px}
.thumbs i{width:50px;height:34px;background:linear-gradient(135deg,#555,#222);display:block}
.thumbs i:nth-child(odd){background:linear-gradient(135deg,#6a7f98,#2b3440)}

/* trainers */
.trainers{height:480px;background:var(--light)}
.trainers .intro{position:absolute;left:100px;top:20px;width:360px;height:340px;background:var(--white);box-shadow:0 2px 14px rgba(0,0,0,.08);padding:44px 36px}
.trainers .intro h3{font-size:15px;color:var(--ink);font-weight:600}
.trainers .intro h2{font-size:24px;color:var(--ink);font-weight:800;margin-top:4px}
.trainers .intro p{font-size:11px;line-height:1.7;color:var(--muted);margin-top:18px}
.trainers .intro .rule{width:40px;height:3px;background:var(--orange);margin-top:20px}
.trainer-list{position:absolute;left:590px;top:120px;display:flex;gap:26px}
.trainer{width:200px;text-align:center}
.trainer .photo{height:220px;background:linear-gradient(180deg,#c9d3de,#5d6b7d)}
.trainer h4{font-size:11px;color:var(--ink);font-weight:700;margin-top:10px}
.dots{position:absolute;left:800px;top:432px;display:flex;gap:6px}
.dots i{width:7px;height:7px;border-radius:50%;background:#bbb;display:block}
.dots i:first-child{background:var(--orange)}

/* brochure */
.brochure{height:120px;background:var(--orange);display:flex;align-items:center;justify-content:space-between;padding:0 290px 0 190px}
.brochure h2{color:var(--white);font-size:22px;font-weight:800}
.brochure p{color:#fde8c7;font-size:11px;margin-top:4px}

/* feedback */
.feedback{height:360px;background:linear-gradient(90deg,#e9e9e9,#d9d9d9 60%,#bfbfbf);text-align:center;padding-top:40px}
.feedback .label{color:var(--ink)}
.feedback p{width:760px;margin:30px auto 0;font-size:12px;line-height:1.7;color:#666}
.feedback .who{margin-top:40px;font-size:10px;color:var(--ink);font-weight:700;letter-spacing:1px}
.feedback .dots{position:static;justify-content:center;margin-top:10px}

/* footer */
.footer{height:420px;background:var(--darker);color:#aaa;padding:40px 100px 0;display:grid;grid-template-columns:300px 330px 300px;gap:35px}
.footer h4{color:var(--white);font-size:14px;font-weight:700;margin-bottom:16px}
.footer p{font-size:11px;line-height:1.7}
.footer .sub{display:flex;margin-top:20px}
.footer .sub span{flex:1;height:30px;background:#2a2a2a;border:1px solid #333}
.footer .sub b{width:36px;height:30px;background:var(--orange)}
.widget{background:var(--white);height:250px;padding:10px}
.widget .head{height:46px;background:linear-gradient(90deg,#4a5568,#2d3748);color:var(--white);font-size:11px;font-weight:700;padding:8px}
.widget .row{display:flex;gap:8px;margin-top:10px}
.widget .row i{width:34px;height:34px;background:#cfd4dc;display:block;flex:none}
.widget .row span{font-size:10px;color:#555;line-height:1.4}
.bottom{height:32px;background:#0b0b0b;color:#777;font-size:10px;display:flex;align-items:center;padding:0 100px}
</style>
</head>
<body>

<header class="hero">
  <div class="topbar">
    <div class="info"><span>☎ (323) 555-0148</span><span>⌖ 1820 Larkmoor Ave, Commerce, CA</span></div>
    <div class="right">
      <span>SECURITY LOGIN &nbsp;|&nbsp; CONTACT &nbsp;|&nbsp; FAQ &nbsp;|&nbsp; BLOG</span>
      <i class="dot"></i><i class="dot"></i><i class="dot"></i>
      <span class="search"><svg width="14" height="14" viewBox="0 0 14 14"><circle cx="6" cy="6" r="4.5" fill="none" stroke="#fff" stroke-width="1.6"/><line x1="9.3" y1="9.3" x2="13" y2="13" stroke="#fff" stroke-width="1.6"/></svg></span>
    </div>
  </div>
  <div class="scene" role="img" aria-label="Modern glass building backdrop with a uniformed security officer standing arms crossed">
    <div class="officer"></div>
  </div>
  <nav class="nav">
    <a href="#">CALIFORNIA GUARD CARD</a>
    <a href="#">FIREARMS TRAINING</a>
    <div class="logo"><i></i>Watchpost Learning Hub</div>
    <a href="#">SECURITY OFFICER ACADEMY</a>
    <a href="#">CAMPUS SECURITY OFFICER</a>
  </nav>
  <div class="promo">
    <div class="tag">WATCHPOST LEARNING HUB</div>
    <div class="box"><b>FREE TRAINING</b> 2X1 Deal<br>Get a <b>Package</b><br>Offers Ends <b>June 10th,this Friday!</b></div>
    <div class="phone"><svg width="22" height="22" viewBox="0 0 24 24"><path d="M6.6 10.8a15 15 0 0 0 6.6 6.6l2.2-2.2c.3-.3.7-.4 1-.2 1.1.4 2.3.6 3.6.6.6 0 1 .4 1 1V20c0 .6-.4 1-1 1A17 17 0 0 1 3 4c0-.6.4-1 1-1h3.5c.6 0 1 .4 1 1 0 1.3.2 2.5.6 3.6.1.3 0 .7-.2 1z" fill="#fff"/></svg>(323) 555-0148</div>
  </div>
</header>

<section class="about">
  <h3>Providing Security Officer Training</h3>
  <h2>ABOUT US</h2>
  <p>Our academy prepares new and experienced guards for real duty with practical classes, licensed instructors and flexible schedules. Students earn state guard cards, firearms permits and campus credentials while building the confidence employers expect. We guide every learner from the first lesson to the first assignment, with career support and honest advice along the way.</p>
  <div class="actions"><a class="btn btn-orange" href="#">Register Now</a><a class="btn btn-outline" href="#">Read More <span class="arr">›</span></a></div>
</section>

<section class="why">
  <div class="label"><small>THIS IS OUR</small><strong>WHY CHOOSE US</strong></div>
  <h2>Security Guard Training in Los Angeles<br>California Guard Card Specialists</h2>
  <div class="features">
    <div class="left">
      <div class="feature"><i class="ico"></i><div><h4>Convenient</h4><p>Day, evening and weekend classes fit around your job and family routine.</p></div></div>
      <div class="feature"><i class="ico"></i><div><h4>Affordable</h4><p>Fair package pricing and bundle deals keep training within easy reach.</p></div></div>
      <div class="feature"><i class="ico"></i><div><h4>Valuable</h4><p>Certifications recognized by employers across the state security industry.</p></div></div>
    </div>
    <div class="badge" role="img" aria-label="Academy shield badge emblem"></div>
    <div class="right">
      <div class="feature"><i class="ico"></i><div><h4>Fast</h4><p>Finish your guard card course in days and start applying right away.</p></div></div>
      <div class="feature"><i class="ico"></i><div><h4>Job Placement</h4><p>Our team connects graduates with hiring partners throughout the region.</p></div></div>
      <div class="feature"><i class="ico"></i><div><h4>Compliance</h4><p>Every course meets current state licensing rules and reporting standards.</p></div></div>
    </div>
  </div>
  <div class="actions"><a class="btn btn-orange" href="#">Register Now</a><a class="btn btn-outline-light" href="#">Call Now <span class="arr">›</span></a><a class="btn btn-outline-light" href="#">Read More <span class="arr">›</span></a></div>
</section>

<section class="courses">
  <div class="label"><small>THIS IS OUR</small><strong>OUR COURSES</strong></div>
  <div class="cards">
    <div class="card"><div class="photo" role="img" aria-label="Officers in a protection training class"></div><i class="ico" style="display:block"></i><h4>CERTIFIED PROTECTION OFFICER (CPO)</h4><p>Core protection skills, patrol methods and report writing for professional officers.</p><a class="btn btn-outline" href="#">Read More</a></div>
    <div class="card"><div class="photo" role="img" aria-label="Firearms instructor at a range"></div><i class="ico" style="display:block"></i><h4>CERTIFIED FIREARMS OFFICER (CFO)</h4><p>Safe handling, range practice and state exposed firearm permit preparation.</p><a class="btn btn-outline" href="#">Read More</a></div>
    <div class="card"><div class="photo" role="img" aria-label="Security officer on duty outdoors"></div><i class="ico" style="display:block"></i><h4>SECURITY OFFICER ACADEMY (SOA)</h4><p>A complete program taking new recruits from basics to job ready status.</p><a class="btn btn-outline" href="#">Read More</a></div>
    <div class="card"><div class="photo" role="img" aria-label="Campus security officers on patrol"></div><i class="ico" style="display:block"></i><h4>CAMPUS SECURITY OFFICER (CSO)</h4><p>Focused training for schools, colleges and university safety teams.</p><a class="btn btn-outline" href="#">Read More</a></div>
  </div>
  <div class="register"><a class="btn btn-orange" href="#">Register Now</a></div>
</section>

<section class="gallery">
  <div class="label"><small>THIS IS OUR</small><strong>OUR GALLERY</strong></div>
  <div class="video" role="img" aria-label="Promotional video: Security offers full time and part time jobs">
    <div class="bar">California Guard Card</div>
    <svg class="play" width="80" height="60" viewBox="0 0 80 60"><circle cx="40" cy="30" r="28" fill="rgba(255,255,255,.25)"/><path d="M32 18v24l20-12z" fill="#fff"/></svg>
  </div>
  <div class="thumbs"><i></i><i></i><i></i><i></i><i></i><i></i><i></i><i></i><i></i><i></i></div>
</section>

<section class="trainers">
  <div class="intro">
    <h3>The Security Guard Training</h3>
    <h2>OUR TRAINERS</h2>
    <p>Our instructors bring years of field experience from law enforcement, private protection and campus safety. They teach with patience, share real cases and coach every student toward licensing success and a lasting career in security.</p>
    <div class="rule"></div>
  </div>
  <div class="trainer-list">
    <div class="trainer"><div class="photo" role="img" aria-label="Portrait of trainer in uniform"></div><h4>MR. DALTON</h4></div>
    <div class="trainer"><div class="photo" role="img" aria-label="Portrait of trainer in uniform"></div><h4>RAVI OKAFOR</h4></div>
  </div>
  <div class="dots"><i></i><i></i><i></i></div>
</section>

<section class="brochure">
  <div><h2>DOWNLOAD OUR BROCHURE</h2><p>Get course dates, prices and schedules in one file.</p></div>
  <a class="btn btn-outline-light" href="#">Brochure ↓</a>
</section>

<section class="feedback" role="img" aria-label="Soft background photo of a student in sunglasses">
  <div class="label"><small>WHAT CLIENTS SAY ABOUT US</small><strong>STUDENTS FEEDBACK</strong></div>
  <p>The instructors were clear, friendly and always ready to help. I passed my guard card exam on the first try and found a full time position within two weeks. The schedule worked with my job, and the staff made every step simple. I recommend this school to anyone starting out.</p>
  <div class="who">STUDENT</div>
  <div class="dots"><i></i><i></i><i></i></div>
</section>

<footer class="footer">
  <div>
    <h4>Watchpost Learning Hub</h4>
    <p>1820 Larkmoor Ave, Commerce,<br>CA, United States<br>(323) 555-0148</p>
    <p style="margin-top:24px">Subscribe to our newsletter for latest updates</p>
    <div class="sub"><span></span><b></b></div>
  </div>
  <div>
    <h4>Community Page</h4>
    <div class="widget"><div class="head">Watchpost Learning Hub</div>
      <div class="row"><i></i><span>New guard card classes open this month. Reserve a seat today.</span></div>
      <div class="row"><i></i><span>Congratulations to our latest firearms graduates.</span></div>
    </div>
  </div>
  <div>
    <h4>Latest Updates</h4>
    <div class="widget"><div class="head">Updates</div>
      <div class="row"><i></i><span>Campus officer course starts Monday morning.</span></div>
      <div class="row"><i></i><span>Weekend academy seats now available.</span></div>
    </div>
  </div>
</footer>
<div class="bottom">© Copyright Watchpost Learning Hub. All rights reserved.</div>

</body>
</html>
```